New travel store signage for Kelvane Journeys to attract luxury travellers.

Hello,
We are looking to change the signage of our stores. The signage must include the following:
1. Kelvane Journeys Logo (attached)
2. The text...The Travel & Cruise Experts
3. Brand Colours ( Fb0196, 412266, d41d84 and ffffff)
Please note the signage design must be central and only cover two thirds of the store front. We have also attached an image of one of our new stores which might be helpful when preparing a mock up.

We are looking for a quick turnaround on this, making a decision within 48 hours.

Target Market(s)

Retail

Industry/Entity Type

Travel Agency

Font styles to use
Other font styles liked:
• Radley

Colors
E54698
E96AAD
F1A4CE
F9D9EA
FCEFF6
6B429C
8869AF
B7A5CE
E3DAEB
F3F0F8

Requirements
Must have
• Hello, We are looking to change the signage of our stores. The signage must include the following: 1. Kelvane Journeys Logo (attached) 2. The text...The Travel & Cruise Experts 3. Brand Colours ( Fb0196, 412266, d41d84 and ffffff) Please note the signage design must be central and only cover two thirds of the store front.
Should not have
• different colour or fonts. Gradient design.

```html
<!DOCTYPE html>
<html lang="en">
<head>
<meta charset="UTF-8">
<title>Kelvane Journeys – Store Signage</title>
<link rel="stylesheet" href="https://fonts.googleapis.com/css2?family=Montserrat:wght@500;600&display=swap">
<style>
  :root {
    --stage-bg: #6a6a6a;
    --brand-navy: #2a1d6a;
    --brand-plum: #412266;
    --brand-magenta: #d41d84;
    --brand-pink: #fb0196;
    --brand-white: #ffffff;
    --wave-line: rgba(255, 255, 255, 0.22);
  }

  * { box-sizing: border-box; margin: 0; padding: 0; }

  html, body {
    width: 997px;
    height: 1200px;
    overflow: hidden;
  }

  body {
    background: var(--stage-bg);
    font-family: "Montserrat", Arial, sans-serif;
    color: var(--brand-white);
    position: relative;
  }

  .store-sign {
    position: absolute;
    left: 34px;
    top: 488px;
    width: 930px;
    height: 223px;
    background: linear-gradient(90deg, var(--brand-navy) 0%, var(--brand-plum) 30%, var(--brand-magenta) 70%, var(--brand-pink) 100%);
    overflow: hidden;
  }

  .sign-wave {
    position: absolute;
    inset: 0;
    width: 100%;
    height: 100%;
  }

  .brand-name {
    position: absolute;
    left: 26px;
    top: 128px;
    display: flex;
    align-items: center;
    gap: 10px;
    font-weight: 600;
    font-size: 25px;
    line-height: 1;
    white-space: nowrap;
  }

  .brand-dot {
    width: 16px;
    height: 16px;
    border-radius: 50%;
    background: var(--brand-white);
    flex: none;
  }

  .headline {
    position: absolute;
    left: 368px;
    top: 16px;
    font-weight: 600;
    line-height: 1;
  }

  .headline-top {
    display: block;
    font-size: 40px;
    letter-spacing: -0.3px;
  }

  .headline-main {
    display: block;
    font-size: 57px;
    letter-spacing: -0.5px;
    margin-top: 6px;
  }

  .web-address {
    position: absolute;
    right: 34px;
    bottom: 12px;
    font-weight: 500;
    font-size: 24px;
    letter-spacing: 0.6px;
    line-height: 1;
  }
</style>
</head>
<body>
  <section class="store-sign" aria-label="Kelvane Journeys store sign">
    <svg class="sign-wave" viewBox="0 0 930 223" preserveAspectRatio="none" aria-hidden="true">
      <path d="M250 223 C 330 170, 430 150, 560 168 S 800 150, 930 140" fill="none" stroke="var(--wave-line)" stroke-width="1"/>
    </svg>

    <div class="brand-name">
      <span class="brand-dot"></span>
      <span>Kelvane Journeys</span>
    </div>

    <h1 class="headline">
      <span class="headline-top">The Travel &amp;</span>
      <span class="headline-main">Cruise Experts</span>
    </h1>

    <p class="web-address">www.kelvanejourneys.com</p>
  </section>
</body>
</html>
```